BrightLedger Mobile Subscription Service

Landing Page for a mobile billed subscription service. In the manner of a slideshow motivate customers to click on "buy" button and do a subscription. HTML5 animation. Per page 2-3 background pictures fading in and out or sliding/focusing. Overlayed text animated as well. Zooming in zooming out. All state of the art design.

Target Market(s)

Switzerland, Germany

Industry/Entity Type

It Service

Number of Pages Required

5+ page

Requirements
Must have
• 5 Pages with sliding pics and text-animation. Delivered as HTML5 animation

```html
<!DOCTYPE html>
<html lang="de">
<head>
<meta charset="utf-8">
<title>BrightLedger – Angebot</title>
<link rel="stylesheet" href="https://fonts.googleapis.com/css2?family=Roboto+Condensed:wght@400;700&display=swap">
<style>
  :root {
    --ink: #ffffff;
    --photo-warm: #8a6a3a;
    --photo-gold: #b8924f;
    --photo-mid: #3a2a18;
    --photo-dark: #120d08;
    --photo-deep: #080604;
  }
  * { margin: 0; padding: 0; box-sizing: border-box; }
  html, body { width: 1200px; height: 593px; overflow: hidden; background: var(--photo-deep); }
  .slide {
    position: relative;
    width: 1200px;
    height: 593px;
    overflow: hidden;
    font-family: "Roboto Condensed", "Arial Narrow", sans-serif;
    color: var(--ink);
  }
  .slide-photo {
    position: absolute;
    inset: 0;
    background:
      radial-gradient(ellipse 230px 260px at 150px 330px, rgba(184,146,79,0.75), transparent 70%),
      radial-gradient(ellipse 160px 240px at 520px 330px, rgba(160,125,70,0.6), transparent 70%),
      radial-gradient(ellipse 420px 120px at 380px 560px, rgba(150,140,125,0.45), transparent 75%),
      radial-gradient(ellipse 200px 300px at 1150px 300px, rgba(90,65,35,0.5), transparent 75%),
      linear-gradient(90deg, var(--photo-warm) 0%, var(--photo-mid) 40%, var(--photo-dark) 62%, var(--photo-deep) 85%, var(--photo-mid) 100%);
  }
  .offer {
    position: absolute;
    left: 724px;
    top: 166px;
  }
  .offer-headline {
    font-weight: 700;
    font-size: 41px;
    line-height: 47px;
    text-transform: uppercase;
    letter-spacing: 0.2px;
  }
  .countdown {
    display: flex;
    gap: 11px;
    margin-top: 18px;
    margin-left: 6px;
  }
  .countdown-unit {
    display: flex;
    flex-direction: column;
    align-items: center;
    width: 57px;
  }
  .countdown-value {
    width: 57px;
    height: 43px;
    border: 1px solid var(--ink);
    display: flex;
    align-items: center;
    justify-content: center;
    font-weight: 700;
    font-size: 27px;
  }
  .countdown-label {
    margin-top: 8px;
    font-weight: 700;
    font-size: 13px;
    text-transform: uppercase;
  }
  .slide-dots {
    display: block;
    margin-top: 18px;
    margin-left: 4px;
  }
</style>
</head>
<body>
  <main class="slide">
    <div class="slide-photo" role="img" aria-label="Photo of champagne glasses on a silver tray in a dim, warmly lit bar"></div>
    <section class="offer">
      <h1 class="offer-headline">Nutze deine Chance<br>jetzt. Dieses Angebot<br>gilt nur noch 72h!</h1>
      <div class="countdown">
        <div class="countdown-unit"><span class="countdown-value">03</span><span class="countdown-label">Day</span></div>
        <div class="countdown-unit"><span class="countdown-value">74</span><span class="countdown-label">Hours</span></div>
        <div class="countdown-unit"><span class="countdown-value">33</span><span class="countdown-label">Minutes</span></div>
        <div class="countdown-unit"><span class="countdown-value">42</span><span class="countdown-label">Seconds</span></div>
      </div>
      <svg class="slide-dots" width="100" height="18" viewBox="0 0 100 18" aria-label="Slide 5 of 5">
        <circle cx="6" cy="9" r="5.5" fill="none" stroke="#fff" stroke-width="1"/>
        <circle cx="26" cy="9" r="5.5" fill="none" stroke="#fff" stroke-width="1"/>
        <circle cx="46" cy="9" r="5.5" fill="none" stroke="#fff" stroke-width="1"/>
        <circle cx="66" cy="9" r="5.5" fill="none" stroke="#fff" stroke-width="1"/>
        <circle cx="86" cy="9" r="7" fill="#fff"/>
      </svg>
    </section>
  </main>
</body>
</html>
```